Regional Sales Company Needs Professional Document Design

We are an American Midwest company that needs clean, polished document layouts that effectively communicate the most critical information to the recipient. This project is specifically for a sales quote, but additional documents (subsequent work) need a consistent look. Our primary design guidelines are: 1) Use the same colors and logos provided. 2) minimize the amount of space the header occupies on the document. 3) Prioritize the information as it has been numbered in the attachment (1 - 5). 4) Redesign the footer logo/image. The information must stay the same, but present it as you see fit.

I have attached a draft and an annotation layout. The draft shows the overall structure and information on the document. The Annotation layout has the numbering referenced and some additional notes.

Industry/Entity Type

HVAC Supplier

Colors
0054AA
0677BA
7BADD7
CADEEF
E8F1F8

Requirements
Must have
• Maintain overall structure of draft. E.g. No left to right documents

```html
<!DOCTYPE html>
<html lang="en">
<head>
<meta charset="utf-8">
<title>Sales Quote – Maple Ridge Health &amp; Rehabilitation</title>
<link rel="stylesheet" href="https://fonts.googleapis.com/css2?family=Montserrat:wght@400;500;600;700&display=swap">
<style>
  :root {
    --navy: #134a87;
    --blue: #0677BA;
    --sky: #7BADD7;
    --pale: #CADEEF;
    --ink: #1b1b1b;
    --grey: #777;
    --paper: #ffffff;
  }
  * { margin: 0; padding: 0; box-sizing: border-box; }
  html, body { width: 757px; height: 1200px; overflow: hidden; background: var(--paper); }
  body { font-family: "Montserrat", Arial, sans-serif; color: var(--ink); }
  .quote { position: relative; width: 757px; height: 1200px; }
  .abs { position: absolute; }
  .shapes { position: absolute; left: 0; top: 0; }

  .brand-box { left: 28px; top: 38px; width: 287px; height: 103px; background: var(--paper);
    display: flex; align-items: center; justify-content: center; }
  .brand-name { font-size: 24px; font-weight: 700; color: var(--navy); white-space: nowrap; }
  .brand-strip { left: 30px; top: 141px; width: 283px; height: 14px; background: var(--navy);
    color: var(--paper); font-size: 8px; font-weight: 600; letter-spacing: 2.2px;
    text-align: center; line-height: 14px; }

  .project-title { left: 359px; top: 40px; font-size: 13.5px; font-weight: 700; letter-spacing: .2px; white-space: nowrap; }
  .project-address { left: 359px; top: 60px; font-size: 10px; color: var(--grey); }
  .meta-label { font-size: 10.5px; font-weight: 700; }
  .meta-value { font-size: 9px; color: var(--grey); }

  .col-head { top: 248px; font-size: 12.5px; font-weight: 700; }

  .maker { font-size: 19px; font-weight: 700; color: var(--navy); display: flex; align-items: center; gap: 6px; }
  .maker-square { width: 20px; height: 20px; background: var(--navy); }
  .qty { font-size: 8.5px; font-weight: 500; }
  .item { font-size: 8.5px; font-weight: 500; line-height: 16.7px; white-space: nowrap; }
  .item .accent { color: var(--blue); }
  .item .sub { padding-left: 10px; }
  .item .sub-accent { padding-left: 10px; color: var(--navy); }
  .basis { font-size: 8.5px; font-weight: 600; color: var(--blue); }

  .total { background: var(--navy); color: var(--paper); font-size: 9px; text-align: center;
    line-height: 1.25; padding-top: 4px; border: 1px solid var(--paper); outline: 1px solid var(--navy); white-space: nowrap; }

  .office-city { font-size: 8px; font-weight: 700; top: 1098px; }
  .office-addr { font-size: 8px; color: var(--grey); top: 1119px; line-height: 12px; white-space: nowrap; }
  .office-phone { font-size: 8px; font-weight: 700; top: 1157px; }

  .footer-tagline { left: 427px; width: 330px; top: 1124px; text-align: center; color: var(--paper);
    font-size: 11px; line-height: 17px; }
</style>
</head>
<body>
<main class="quote">
  <svg class="shapes" width="757" height="1200" viewBox="0 0 757 1200" aria-hidden="true">
    <rect x="0" y="0" width="757" height="18" fill="var(--navy)"/>
    <polygon points="0,0 356,0 347,182 0,182" fill="var(--navy)"/>
    <rect x="340" y="183" width="417" height="4" fill="var(--navy)"/>
    <polygon points="0,1053 419,1053 416,1058 0,1058" fill="var(--navy)"/>
    <polygon points="430,1088 757,1088 757,1200 392,1200" fill="var(--navy)"/>
    <rect x="0" y="1182" width="757" height="18" fill="var(--navy)"/>
  </svg>

  <header>
    <div class="abs brand-box"><span class="brand-name">Northline Supply Co.</span></div>
    <div class="abs brand-strip">LAKEPORT - RIVERTON - MILLBROOK</div>

    <h1 class="abs project-title">MAPLE RIDGE HEALTH &amp; REHABILITATION</h1>
    <p class="abs project-address">1850 Harwick Park Drive, Brookhaven, OH, 44790</p>

    <div class="abs meta-label" style="left:359px;top:88px">Quote:</div>
    <div class="abs meta-value" style="left:359px;top:109px">Q000039</div>
    <div class="abs meta-label" style="left:433px;top:88px">Engineer:</div>
    <div class="abs meta-value" style="left:433px;top:109px">KRT Engineering</div>
    <div class="abs meta-label" style="left:538px;top:88px">Quote Date:</div>
    <div class="abs meta-value" style="left:538px;top:109px">12/31/2024</div>
    <div class="abs meta-label" style="left:632px;top:88px">Project Bid Date:</div>
    <div class="abs meta-value" style="left:632px;top:109px">12/31/2024</div>

    <div class="abs meta-label" style="left:359px;top:140px">Plan Date:</div>
    <div class="abs meta-value" style="left:359px;top:161px">12/31/2024</div>
    <div class="abs meta-label" style="left:433px;top:140px">Quote Rev:</div>
    <div class="abs meta-value" style="left:433px;top:161px">00</div>
    <div class="abs meta-label" style="left:538px;top:140px">Addendum:</div>
    <div class="abs meta-value" style="left:538px;top:161px">1</div>
  </header>

  <div class="abs col-head" style="left:116px">MANUFACTURER</div>
  <div class="abs col-head" style="left:523px">QTY DESCRIPTION</div>

  <div class="abs maker" style="left:27px;top:316px"><span class="maker-square"></span>Norvane</div>
  <div class="abs qty" style="left:201px;top:355px">463</div>
  <div class="abs item" style="left:228px;top:349px">
    Pieces of Norvane Air Distribution with Standard White Finish<br>
    <span class="sub">•Dampers included per the schedule IF there is NO CRD</span><br>
    <span class="sub">•If a Grille has a CRD, NO OBD included (see CRD's)</span><br>
    Estimated Lead-time to ship: 3-4 weeks + Transit Time from Factory
  </div>
  <div class="abs basis" style="left:228px;top:430px">Norvane Industries Inc. is Basis of Design</div>
  <div class="abs total" style="left:586px;top:427px;width:141px;height:38px">Total with Full Freight Allowed<br>$18,850</div>

  <div class="abs maker" style="left:27px;top:496px"><span class="maker-square"></span>Hollisfield</div>
  <div class="abs qty" style="left:201px;top:529px">2</div>
  <div class="abs item" style="left:216px;top:523px">
    Hollisfield DOAS Units <span class="accent">(Dedicated Outdoor Air System)</span> with Weatherhood, Return Air Intake,<br>
    Expansion Board, Frost control, Outdoor/Exhaust MERV8 Filters, Supply MERV13 Filters, Outdoor<br>
    Dampers, End Switch, Painted Finish, VFD Control, Economizer, Microprocessor Controls,<br>
    Duct Sensors, Dirty Filter Sensor, Rotation Sensor, Phase and Brown Out Protection,<br>
    Disconnect Switch, Hail Guards, Condensate Overflow Switch, Spare Energy Wheel Belt,<br>
    12:1 Turndown, DX Cooling, Inverter Scroll Compressor, Modulating Hot Gas, Reheat,<br>
    Lead EC Condenser Fan and 14" High FLAT Roof Curbs per Note 18 (DOAS-1,2)<br>
    <span class="sub-accent">•Includes Unit Warranty &amp; Labor Warranty</span><br>
    NOTE: Duct Adapter is NOT included - removed by HF<br>
    Estimated Lead-time to ship: <span class="accent">9 weeks + Transit Time from Factory</span>
  </div>
  <div class="abs basis" style="left:216px;top:719px">Hollisfield Fan Corporation is Basis of Design</div>
  <div class="abs total" style="left:586px;top:722px;width:141px;height:38px">Total with Full Freight Allowed<br>$157,000</div>

  <div class="abs maker" style="left:27px;top:806px"><span class="maker-square"></span>Hollisfield</div>
  <div class="abs qty" style="left:198px;top:838px">1</div>
  <div class="abs item" style="left:216px;top:832px">ADD - for DOAS Start-Up and Start-Up Dispatch</div>
  <div class="abs total" style="left:593px;top:835px;width:130px;height:36px">Price includes (1) trip charge<br>$2,550</div>

  <footer>
    <div class="abs office-city" style="left:27px">RIVERTON</div>
    <div class="abs office-addr" style="left:27px">2240 Linden Avenue<br>Riverton, Oh 43901</div>
    <div class="abs office-phone" style="left:27px">614.555.0147</div>

    <div class="abs office-city" style="left:151px">LAKEPORT</div>
    <div class="abs office-addr" style="left:151px">4100 Canal Road<br>Lakeport Heights, Oh 44902</div>
    <div class="abs office-phone" style="left:151px">440.555.0120</div>

    <div class="abs office-city" style="left:297px">MILLBROOK</div>
    <div class="abs office-addr" style="left:297px">7700 S. Ashford Way<br>Millbrook, Oh 43903</div>
    <div class="abs office-phone" style="left:297px">419.555.0190</div>

    <p class="abs footer-tagline">BUILT AROUND YOUR PROJECT<br>Reliable Equipment and Support</p>
  </footer>
</main>
</body>
</html>
```